Design a Hemp Museum + exhibition design**

I'm creating an Online Museum for Hemp which will tell the story of hemp from ancient times to now and the future
cover the medical, industrial and nutritional uses and development of hemp
the people behind it, researchers, politicians, farmers and influencerts

the museum will have a number of "wings" , each holds an exhibition around a differnet theme, for example:

Hemp in the Age of Empires: 18th and 19th Century Collections
Hemp - The History of Healing
Domestication and Early Use: Ancient Collection
From Cotton Gin to Plastics and Prohibition: Hemp's Decline

these are just a few sample ideas for exhibitions

I'm looking for an overall design for the museum home page and exhibition page which will make people curious and want to spend time,learning and browsing

Think mobile -first :)

You are requested to design

1. Home page
2. Exhibition page

Target Market(s)

Hemp aficionados, curious fans

Logo Text

The Lumen Museum

Coding

Coded - Design and coding required

Number of Pages Required

3 page

Font styles to use
Sans Serif
Decorative

Requirements
Must have
• a homepage design which prompts visitors to immediately start watching an exhibition

visitors need to understand that this is a museum , so that they dont think it's a business, a service provider or anything like that

needs to have the usual links to T&C, privacy, about us

needs to have a link to "Wander past the lantern stall"

must have a visual WOW effect
Nice to have
• animations, sounds etc
Should not have
• forms like contact us etc - not relevant

```html
<!DOCTYPE html>
<html lang="en">
<head>
<meta charset="utf-8">
<title>Lumen Hall – The Lumen Museum</title>
<link href="https://fonts.googleapis.com/css2?family=Roboto:ital,wght@0,400;0,500;0,700;0,900;1,500&display=swap" rel="stylesheet">
<style>
:root{
  --green:#5c9a2c;
  --green-bright:#6cb633;
  --green-dark:#3f7a1c;
  --ink:#222222;
  --text:#555555;
  --muted:#777777;
  --white:#ffffff;
  --footer:#1c1c1c;
  --footer-line:#3a3a3a;
}
*{box-sizing:border-box;margin:0;padding:0}
html,body{width:1200px;height:5272px;overflow:hidden}
body{font-family:'Roboto',Arial,sans-serif;color:var(--text);background:var(--white);position:relative}
.section{position:absolute;left:0;width:1200px}
.section-title{font-size:36px;font-weight:700;color:var(--ink);text-align:center;width:1200px;position:absolute;left:0}
.title-rule{position:absolute;left:560px;width:80px;height:3px;background:var(--green-bright)}

/* hero */
.hero{top:0;height:760px;overflow:hidden}
.hero-photo{position:absolute;inset:0;background:linear-gradient(120deg,#5d6b45 0%,#3f5a2a 35%,#6d8a48 60%,#2f4a20 100%)}
.hero-shade{position:absolute;inset:0;background:rgba(0,0,0,.25)}
.wordmark{position:absolute;left:143px;top:50px;font-size:30px;font-weight:500;color:var(--white);letter-spacing:.5px}
.call{position:absolute;left:588px;top:54px;display:flex;align-items:center;gap:14px;color:var(--white)}
.call-icon{width:36px;height:36px;border-radius:50%;background:var(--green-bright);display:flex;align-items:center;justify-content:center}
.call small{display:block;font-size:13px;font-weight:500}
.call strong{display:block;font-size:19px;font-weight:700}
.quote-btn{position:absolute;left:813px;top:51px;width:184px;height:44px;border-radius:22px;background:var(--green-bright);color:var(--white);font-size:15px;font-weight:700;display:flex;align-items:center;justify-content:center}
.menu{position:absolute;left:1030px;top:60px;width:26px}
.menu span{display:block;height:4px;background:var(--white);margin-bottom:5px;border-radius:1px}
.hero-title{position:absolute;left:0;width:1200px;top:306px;text-align:center;font-size:58px;font-weight:700;color:var(--white)}
.hero-text{position:absolute;left:275px;width:650px;top:384px;text-align:center;font-size:17px;line-height:25px;color:var(--white)}
.hero-btn{position:absolute;left:471px;top:485px;width:258px;height:42px;border-radius:21px;background:var(--green-bright);color:var(--white);font-size:15px;font-weight:500;display:flex;align-items:center;justify-content:center}
.dots{position:absolute;top:652px;left:564px;display:flex;gap:9px}
.dots span{width:18px;height:18px;border-radius:50%;border:2px solid var(--white)}
.hero-curve{position:absolute;left:0;bottom:0}

/* map wings */
.wings{top:760px;height:683px}
.wing-list{position:absolute;left:123px;top:208px;width:960px;display:flex;justify-content:space-between}
.wing{width:230px;text-align:center}
.wing-photo{width:212px;height:212px;border-radius:50%;margin:0 auto;border:6px solid var(--white);box-shadow:0 4px 14px rgba(0,0,0,.25)}
.wing-title{margin:36px auto 0;width:205px;font-size:17px;line-height:24px;color:var(--ink);height:72px}
.wing-title b{color:var(--green);font-weight:700}
.wing:nth-child(even) .wing-title{height:56px}
.outline-btn{display:inline-flex;align-items:center;justify-content:center;border:2px solid var(--green-bright);border-radius:22px;color:var(--green);font-size:12px;font-weight:700}
.wing .outline-btn{width:146px;height:40px;margin-top:16px}

/* feature bands */
.band{height:528px;overflow:hidden}
.band-welcome{top:1443px}
.band-stall{top:1971px;height:489px}
.band-photo{position:absolute;top:0;height:100%}
.band-green{position:absolute;top:0;height:100%;background:var(--green)}
.band h2{position:absolute;font-size:36px;font-weight:500;color:var(--white);white-space:nowrap}
.band .rule{position:absolute;width:58px;height:4px;background:var(--white)}
.band p{position:absolute;font-size:15.5px;line-height:24px;color:#eef5e6}
.band .ghost-btn{position:absolute;width:162px;height:43px;border:2px solid var(--white);border-radius:22px;color:var(--white);font-size:13px;font-weight:700;display:flex;align-items:center;justify-content:center}

/* future */
.future{top:2460px;height:892px}
.future-grid{position:absolute;left:143px;top:190px;width:913px;display:grid;grid-template-columns:repeat(3,285px);column-gap:29px;row-gap:30px}
.future-card{height:283px;background:var(--white);box-shadow:0 3px 16px rgba(0,0,0,.12);text-align:center;padding-top:38px}
.future-icon{width:98px;height:98px;border-radius:50%;border:3px solid var(--green);margin:0 auto;display:flex;align-items:center;justify-content:center}
.future-card h3{margin-top:30px;font-size:15px;font-weight:500;color:var(--ink);letter-spacing:.3px}
.future-card p{margin:16px auto 0;width:220px;font-size:14px;line-height:21px;color:var(--muted)}

/* blog */
.blog{top:3352px;height:782px;background:linear-gradient(180deg,#f4f3ef 0%,#c9c2a2 30%,#9b9a66 60%,#8a8a58 100%)}
.blog-grid{position:absolute;left:143px;top:178px;width:913px;display:grid;grid-template-columns:449px 449px;column-gap:15px;row-gap:20px}
.post{height:246px;background:var(--white);display:flex;position:relative}
.post-photo{width:225px;height:246px}
.post-date{position:absolute;left:190px;top:34px;width:48px;height:48px;border-radius:50%;background:var(--green-bright);border:3px solid var(--white);color:var(--white);font-size:10px;font-weight:700;line-height:11px;display:flex;align-items:center;justify-content:center;text-align:center}
.post-body{padding:30px 20px 0 28px;width:224px}
.post-body h3{font-size:12.5px;font-weight:500;line-height:20px;color:var(--ink)}
.post-body p{margin-top:6px;font-size:12.5px;line-height:18.5px;color:var(--text)}
.post-body a{display:block;margin-top:12px;font-size:11.5px;font-weight:700;color:var(--green-bright);text-decoration:none}

/* testimonials */
.clients{top:4134px;height:655px;background:linear-gradient(180deg,#ffffff 70%,#f1f1f1 100%)}
.client-list{position:absolute;left:143px;top:239px;width:913px;display:flex;justify-content:space-between}
.client{width:276px;text-align:center;position:relative}
.client-card{height:246px;background:var(--white);box-shadow:0 3px 16px rgba(0,0,0,.12);padding:74px 26px 0}
.client-card p{font-size:13.5px;line-height:19.5px;color:var(--text)}
.avatar{position:absolute;left:97px;top:-41px;width:82px;height:82px;border-radius:50%;background:radial-gradient(circle at 50% 40%,#c9a88d,#6b4a3a)}
.avatar-quote{position:absolute;left:127px;top:36px;color:var(--green-bright);font-size:28px;font-weight:900;line-height:20px}
.client-name{margin-top:38px;font-size:15px;font-style:italic;font-weight:500;color:var(--green-bright)}
.stars{margin-top:18px;display:flex;justify-content:center}

/* footer */
.footer{top:4789px;height:483px;background:var(--footer);color:#cfcfcf}
.footer-name{position:absolute;left:143px;top:66px;font-size:26px;font-weight:500;color:var(--white);letter-spacing:.5px}
.footer-about{position:absolute;left:143px;top:112px;width:345px;font-size:14.5px;line-height:23px}
.socials{position:absolute;left:146px;top:252px;display:flex;gap:13px}
.socials span{width:37px;height:37px;border-radius:50%;border:2px solid var(--green-bright)}
.footer-divider{position:absolute;top:70px;width:1px;height:230px;background:var(--footer-line)}
.footer h4{position:absolute;font-size:18px;font-weight:700;color:var(--white)}
.contact-item{position:absolute;left:610px;display:flex;align-items:center;gap:20px}
.contact-icon{width:44px;height:44px;border-radius:50%;border:2px solid #d8d8d8;display:flex;align-items:center;justify-content:center}
.contact-item b{display:block;font-size:15px;font-weight:700;color:var(--white)}
.contact-item span{display:block;font-size:15px;margin-top:4px}
.quick-links{position:absolute;left:948px;top:117px;list-style:none}
.quick-links li{font-size:13.5px;line-height:27.5px;color:#e5e5e5}
.copyright{position:absolute;left:0;top:358px;width:1200px;border-top:1px solid var(--footer-line);padding-top:52px;text-align:center;font-size:14.5px;color:#e5e5e5}
</style>
</head>
<body>

<svg width="0" height="0" style="position:absolute">
  <defs>
    <path id="star" d="M7 1l1.8 4 4.2.4-3.2 2.8 1 4.2L7 10.2 3.2 12.4l1-4.2L1 5.4l4.2-.4z"/>
  </defs>
</svg>

<header class="section hero">
  <div class="hero-photo" role="img" aria-label="Researcher in a white coat inspecting tall hemp plants in a field"></div>
  <div class="hero-shade"></div>
  <div class="wordmark">Lumen Hall</div>
  <div class="call">
    <div class="call-icon">
      <svg width="18" height="18" viewBox="0 0 24 24"><path fill="#fff" d="M6.6 10.8a15.1 15.1 0 0 0 6.6 6.6l2.2-2.2c.3-.3.7-.4 1-.2 1.1.4 2.3.6 3.6.6.6 0 1 .4 1 1V20c0 .6-.4 1-1 1A17 17 0 0 1 3 4c0-.6.4-1 1-1h3.5c.6 0 1 .4 1 1 0 1.3.2 2.5.6 3.6.1.3 0 .7-.2 1z"/></svg>
    </div>
    <div><small>Call us</small><strong>555 0142 0199</strong></div>
  </div>
  <div class="quote-btn">FREE QUOTE</div>
  <div class="menu"><span></span><span></span><span></span></div>
  <h1 class="hero-title">The Lumen Museum</h1>
  <p class="hero-text">Sed ut perspiciatis unde omnis iste natus error sit voluptatem accusantium doloremque laudantium, totam rem aperiam, eaque ipsa quae ab illo inventore veritatis et quasi architecto</p>
  <div class="hero-btn">Wander past the lantern stall</div>
  <div class="dots"><span></span><span></span><span></span></div>
  <svg class="hero-curve" width="1200" height="110" viewBox="0 0 1200 110">
    <path fill="#5c9a2c" d="M0 12 Q520 70 960 108 L1200 40 L1200 110 L0 110 Z"/>
    <path fill="#ffffff" d="M0 42 Q500 95 960 110 Q1080 60 1200 20 L1200 110 L0 110 Z"/>
  </svg>
</header>

<section class="section wings">
  <h2 class="section-title" style="top:72px">Map to the Lumen Museum</h2>
  <div class="title-rule" style="top:146px"></div>
  <div class="wing-list">
    <div class="wing">
      <div class="wing-photo" style="background:radial-gradient(circle at 40% 60%,#7fb04a,#3f6a24)" role="img" aria-label="Hand holding a young hemp plant"></div>
      <div class="wing-title"><b>Hemp in the Age of Empires:</b> 18th and 19th Century Collections</div>
      <span class="outline-btn">Learn More &gt;</span>
    </div>
    <div class="wing">
      <div class="wing-photo" style="background:radial-gradient(circle at 50% 50%,#e6ecef,#8fa4ad)" role="img" aria-label="Scientist working in a laboratory"></div>
      <div class="wing-title"><b>Hemp -</b> The History of Healing</div>
      <span class="outline-btn">Learn More &gt;</span>
    </div>
    <div class="wing">
      <div class="wing-photo" style="background:radial-gradient(circle at 50% 50%,#5d8a3c,#1f3a16)" role="img" aria-label="Close view of hemp leaves and flowers"></div>
      <div class="wing-title"><b>Domestication and Early Use:</b> Ancient Collection</div>
      <span class="outline-btn">Learn More &gt;</span>
    </div>
    <div class="wing">
      <div class="wing-photo" style="background:radial-gradient(circle at 60% 30%,#c9a86a,#4d7a2e 60%)" role="img" aria-label="Farmer in a straw hat tending hemp crops"></div>
      <div class="wing-title"><b>From Cotton Gin to Plastics and Prohibition:</b> Hemp's Decline</div>
      <span class="outline-btn">Learn More &gt;</span>
    </div>
  </div>
</section>

<section class="section band band-welcome">
  <div class="band-photo" style="left:0;width:1200px;background:radial-gradient(circle at 75% 50%,#ffffff,#d6d6d6 70%)" role="img" aria-label="Human head silhouette formed from hemp leaves"></div>
  <div class="band-green" style="left:0;width:632px;clip-path:polygon(0 0,100% 0,71% 100%,0 100%)"></div>
  <h2 style="left:143px;top:82px">Welcome to Lumen Hall</h2>
  <div class="rule" style="left:143px;top:152px"></div>
  <p style="left:143px;top:182px;width:370px">Sed ut perspiciatis unde omnis iste natus error sit voluptatem accusantium doloremque laudantium, totam rem aperiam, eaque ipsa quae ab illo inventore veritatis et quasi architecto beatae vitae dicta sunt explicabo. Nemo enim ipsam voluptatem quia voluptas sit aspernatur aut odit aut fugit, sed quia consequuntur magni dolores eos qui ratione</p>
  <div class="ghost-btn" style="left:143px;top:395px">LEARN MORE</div>
</section>

<section class="section band band-stall">
  <div class="band-photo" style="left:0;width:1200px;background:linear-gradient(100deg,#e9ecef 0%,#bfc7c9 25%,#5d7e3a 45%,#2e3f8a 55%,#d8dde0 75%)" role="img" aria-label="Gloved hands holding hemp leaves beside a small bottle of oil"></div>
  <div class="band-green" style="left:572px;width:628px;clip-path:polygon(0 0,100% 0,100% 100%,17% 100%)"></div>
  <h2 style="left:725px;top:62px">Wander past the lantern stall</h2>
  <div class="rule" style="left:725px;top:127px"></div>
  <p style="left:725px;top:166px;width:355px">Sed ut perspiciatis unde omnis iste natus error sit voluptatem accusantium doloremque laudantium, totam rem aperiam, eaque ipsa quae ab illo inventore veritatis et quasi architecto beatae vitae dicta sunt explicabo. Nemo enim ipsam voluptatem quia voluptas sit aspernatur aut odit aut fugit, sed quia consequuntur magni</p>
  <div class="ghost-btn" style="left:725px;top:370px">LEARN MORE</div>
</section>

<section class="section future">
  <h2 class="section-title" style="top:68px">Lumen Hall Future</h2>
  <div class="title-rule" style="top:134px"></div>
  <div class="future-grid">
    <div class="future-card">
      <div class="future-icon"><svg width="50" height="50" viewBox="0 0 50 50" fill="none" stroke="#333" stroke-width="2"><path d="M8 44h36M12 44V32h5v12M21 44V26h5v18M30 44V20h5v24M39 44V12h5v32"/><path d="M10 24l10-8 9 4 13-12"/></svg></div>
      <h3>DEVELOPMENT OF HEMP</h3>
      <p>Sed ut perspiciatis unde omnis iste natus error sit voluptatem accusantium doloremque</p>
    </div>
    <div class="future-card">
      <div class="future-icon"><svg width="50" height="50" viewBox="0 0 50 50" fill="none" stroke="#333" stroke-width="2"><path d="M6 44h38M8 44V28l10-6v6l10-6v6l10-6v22"/><path d="M12 10h5v14M32 8h5v12"/><rect x="13" y="34" width="5" height="5"/><rect x="24" y="34" width="5" height="5"/><rect x="35" y="34" width="5" height="5"/></svg></div>
      <h3>INDUSTRIAL &amp; NUTRITIONAL</h3>
      <p>Sed ut perspiciatis unde omnis iste natus error sit voluptatem accusantium doloremque</p>
    </div>
    <div class="future-card">
      <div class="future-icon"><svg width="50" height="50" viewBox="0 0 50 50" fill="none" stroke="#333" stroke-width="2"><circle cx="22" cy="16" r="8"/><path d="M6 44c0-10 7-16 16-16s12 4 14 8"/><circle cx="36" cy="38" r="7"/><path d="M36 34v8M32 38h8"/></svg></div>
      <h3>MEDICAL</h3>
      <p>Sed ut perspiciatis unde omnis iste natus error sit voluptatem accusantium doloremque</p>
    </div>
    <div class="future-card">
      <div class="future-icon"><svg width="50" height="50" viewBox="0 0 50 50" fill="none" stroke="#333" stroke-width="2"><rect x="10" y="6" width="26" height="34"/><path d="M10 44h30"/><circle cx="24" cy="20" r="7"/><path d="M29 25l8 8"/></svg></div>
      <h3>RESEARCHERS</h3>
      <p>Sed ut perspiciatis unde omnis iste natus error sit voluptatem accusantium doloremque</p>
    </div>
    <div class="future-card">
      <div class="future-icon"><svg width="50" height="50" viewBox="0 0 50 50" fill="none" stroke="#333" stroke-width="2"><circle cx="25" cy="16" r="6"/><path d="M15 32c0-6 4-10 10-10s10 4 10 10"/><path d="M8 32h34v4H8zM12 36v8M38 36v8"/><path d="M30 6h12v8H34l-3 3"/></svg></div>
      <h3>POLITICIANS</h3>
      <p>Sed ut perspiciatis unde omnis iste natus error sit voluptatem accusantium doloremque</p>
    </div>
    <div class="future-card">
      <div class="future-icon"><svg width="50" height="50" viewBox="0 0 50 50" fill="none" stroke="#333" stroke-width="2"><circle cx="20" cy="10" r="5"/><path d="M14 44l4-14 6 4v10M18 30l2-12 10 6M30 24l8-14M34 6c4 0 6 3 6 6"/><path d="M6 44h38"/></svg></div>
      <h3>FARMERS AND INFLUENCERS</h3>
      <p>Sed ut perspiciatis unde omnis iste natus error sit voluptatem accusantium doloremque</p>
    </div>
  </div>
</section>

<section class="section blog" role="img" aria-label="Hemp field with a farmer in the background">
  <h2 class="section-title" style="top:64px">Latest Blog</h2>
  <div class="blog-grid">
    <article class="post">
      <div class="post-photo" style="background:linear-gradient(135deg,#9cc66a,#3f6e26)" role="img" aria-label="Glass jar with a hemp sprout"></div>
      <div class="post-date">JAN<br>2021</div>
      <div class="post-body">
        <h3>NEMO ENIM IPSAM VOLUPTATEM QUIA VOLUP TAS SIT IPSAM</h3>
        <p>Sed ut perspiciatis unde omnis iste natus error sit voluptatem accusantium doloremque laudantium, totam rem aperiam, eaque</p>
        <a>READ MORE &gt;&gt;</a>
      </div>
    </article>
    <article class="post">
      <div class="post-photo" style="background:linear-gradient(135deg,#cfe0ec,#4a6ec0 45%,#6c9a3a)" role="img" aria-label="Dropper above a bottle of hemp oil"></div>
      <div class="post-date">JAN<br>2021</div>
      <div class="post-body">
        <h3>NEMO ENIM IPSAM VOLUPTATEM QUIA VOLUP TAS SIT IPSAM</h3>
        <p>Sed ut perspiciatis unde omnis iste natus error sit voluptatem accusantium doloremque laudantium, totam rem aperiam, eaque</p>
        <a>READ MORE &gt;&gt;</a>
      </div>
    </article>
    <article class="post">
      <div class="post-photo" style="background:linear-gradient(135deg,#8a6b4a,#d8d8d8 45%,#4f7a2e)" role="img" aria-label="Researcher with a microscope among hemp plants"></div>
      <div class="post-date">JAN<br>2021</div>
      <div class="post-body">
        <h3>NEMO ENIM IPSAM VOLUPTATEM QUIA VOLUP TAS SIT IPSAM</h3>
        <p>Sed ut perspiciatis unde omnis iste natus error sit voluptatem accusantium doloremque laudantium, totam rem aperiam, eaque</p>
        <a>READ MORE &gt;&gt;</a>
      </div>
    </article>
    <article class="post">
      <div class="post-photo" style="background:linear-gradient(135deg,#e8ecea,#a8c890 50%,#5c8a3a)" role="img" aria-label="Gloved hand holding a test tube with hemp extract"></div>
      <div class="post-date">JAN<br>2021</div>
      <div class="post-body">
        <h3>NEMO ENIM IPSAM VOLUPTATEM QUIA VOLUP TAS SIT IPSAM</h3>
        <p>Sed ut perspiciatis unde omnis iste natus error sit voluptatem accusantium doloremque laudantium, totam rem aperiam, eaque</p>
        <a>READ MORE &gt;&gt;</a>
      </div>
    </article>
  </div>
</section>

<section class="section clients">
  <h2 class="section-title" style="top:74px">What Clients Say</h2>
  <div class="client-list">
    <div class="client">
      <div class="client-card"><p>Sed ut perspiciatis unde omnis iste natus error sit voluptatem accusantium doloremque laudantium, totam rem aperiam, eaque ipsa quae ab illo inventore veritatis et quasi architecto beatae vitae dicta sunt explicabo. Nemo enim ipsam voluptatem quia</p></div>
      <div class="avatar" role="img" aria-label="Portrait of the reviewer"></div>
      <div class="avatar-quote">&#8220;</div>
      <div class="client-name">Marla - Lumen Hall</div>
      <div class="stars"><svg width="108" height="14" viewBox="0 0 108 14" fill="none" stroke="#555" stroke-width="1.2"><use href="#star"/><use href="#star" x="23"/><use href="#star" x="46"/><use href="#star" x="69"/><use href="#star" x="92"/></svg></div>
    </div>
    <div class="client">
      <div class="client-card"><p>Sed ut perspiciatis unde omnis iste natus error sit voluptatem accusantium doloremque laudantium, totam rem aperiam, eaque ipsa quae ab illo inventore veritatis et quasi architecto beatae vitae dicta sunt explicabo. Nemo enim ipsam voluptatem quia</p></div>
      <div class="avatar" role="img" aria-label="Portrait of the reviewer"></div>
      <div class="avatar-quote">&#8220;</div>
      <div class="client-name">Marla - Lumen Hall</div>
      <div class="stars"><svg width="108" height="14" viewBox="0 0 108 14" fill="none" stroke="#555" stroke-width="1.2"><use href="#star"/><use href="#star" x="23"/><use href="#star" x="46"/><use href="#star" x="69"/><use href="#star" x="92"/></svg></div>
    </div>
    <div class="client">
      <div class="client-card"><p>Sed ut perspiciatis unde omnis iste natus error sit voluptatem accusantium doloremque laudantium, totam rem aperiam, eaque ipsa quae ab illo inventore veritatis et quasi architecto beatae vitae dicta sunt explicabo. Nemo enim ipsam voluptatem quia</p></div>
      <div class="avatar" style="background:radial-gradient(circle at 50% 40%,#e0c4a8,#3d5a7a)" role="img" aria-label="Portrait of the reviewer"></div>
      <div class="avatar-quote">&#8220;</div>
      <div class="client-name">Marla - Lumen Hall</div>
      <div class="stars"><svg width="108" height="14" viewBox="0 0 108 14" fill="none" stroke="#555" stroke-width="1.2"><use href="#star"/><use href="#star" x="23"/><use href="#star" x="46"/><use href="#star" x="69"/><use href="#star" x="92"/></svg></div>
    </div>
  </div>
</section>

<footer class="section footer">
  <div class="footer-name">Lumen Hall</div>
  <p class="footer-about">Sed ut perspiciatis unde omnis iste natus error sit voluptatem accusantium doloremque laudantium, totam rem aperiam, eaque ipsa quae ab illo inventore veritatis et quasi architecto beatae vitae dicta sunt explicabo.</p>
  <div class="socials"><span></span><span></span><span></span></div>
  <div class="footer-divider" style="left:541px"></div>
  <div class="footer-divider" style="left:893px"></div>
  <h4 style="left:610px;top:72px">CONTACT US</h4>
  <div class="contact-item" style="top:124px">
    <div class="contact-icon"><svg width="18" height="18" viewBox="0 0 24 24"><path fill="#fff" d="M6.6 10.8a15.1 15.1 0 0 0 6.6 6.6l2.2-2.2c.3-.3.7-.4 1-.2 1.1.4 2.3.6 3.6.6.6 0 1 .4 1 1V20c0 .6-.4 1-1 1A17 17 0 0 1 3 4c0-.6.4-1 1-1h3.5c.6 0 1 .4 1 1 0 1.3.2 2.5.6 3.6.1.3 0 .7-.2 1z"/></svg></div>
    <div><b>PHONE</b><span>555 0142 0199</span></div>
  </div>
  <div class="contact-item" style="top:196px">
    <div class="contact-icon"><svg width="20" height="16" viewBox="0 0 20 16" fill="none" stroke="#fff" stroke-width="1.8"><rect x="1" y="1" width="18" height="14" rx="1"/><path d="M1 2l9 7 9-7"/></svg></div>
    <div><b>EMAIL</b><span>info@lumenhall.example</span></div>
  </div>
  <h4 style="left:946px;top:72px">QUICK LINKS</h4>
  <ul class="quick-links">
    <li>Home</li><li>About</li><li>Terms &amp; Conditions</li><li>Contact</li><li>Privacy Policy</li>
  </ul>
  <div class="copyright">Lumen Hall © 2021.All Rights Reserved</div>
</footer>

</body>
</html>
```